Business Card Design for Tax Accounting Company

I need design files that can be edited to add new professional designations onto the end of my name once complete. I need design files that can be edited for new employees. I also need the design files to be able to upload into PrintHollow for new orders. I've attached multiple logo files with varying file extensions to help with the design.
Please include the following contact information:
Marcus Tenley, CFP®, EA, CTC, CEPA
Founder & CEO
C (480) 517.3082
F (623) 391.7258
418 W Larkspur Ave
Mesa, AZ 85201
Updates
I need the business card to include the following contact info:
C: (480)517.3082
F: (623) 391.7258
mt@QuarrystoneLedgerworks.com
www.MarcusRTenley.com
Address to be included is
418 W Larkspur Ave
Mesa, AZ 85201
Business Cards are double sided
Target Market(s)
Business owners $1M+ annual revenue, especially for the construction and technology industries
Industry/Entity Type
Accounting & Tax
Contact Information for Business Card
Contact information and logo
Look and feel

```html
<!DOCTYPE html>
<html lang="en">
<head>
<meta charset="utf-8">
<title>Quarrystone Ledgerworks – Business Card</title>
<link href="https://fonts.googleapis.com/css2?family=Gelasio:ital,wght@0,400;0,700;1,400;1,700&display=swap" rel="stylesheet">
<style>
  :root {
    --navy: #1c2a5b;
    --red: #b31b2c;
    --orange: #c8582a;
    --gold: #e6c312;
    --paper: #ecebec;
    --backdrop: #c9c9c9;
  }
  * { margin: 0; padding: 0; box-sizing: border-box; }
  html, body { width: 1200px; height: 1101px; overflow: hidden; }
  body {
    background: var(--backdrop);
    font-family: "Gelasio", Georgia, serif;
    position: relative;
  }
  .card {
    position: absolute;
    top: 266px;
    width: 302px;
    height: 533px;
  }
  .card-front { left: 246px; background: var(--paper); color: var(--navy); }
  .card-back { left: 642px; background: var(--navy); color: #e9e9ee; }

  .brand {
    position: absolute; top: 62px; left: 0; width: 100%;
    text-align: center;
  }
  .brand-mark {
    width: 62px; height: 62px; border-radius: 50%;
    background: var(--gold); margin: 0 auto 12px;
  }
  .brand-name {
    font-weight: 700; font-size: 19px; line-height: 21px; color: var(--navy);
  }
  .divider {
    position: absolute; left: 50%; width: 86px; height: 2px;
    margin-left: -43px; background: var(--navy); border-radius: 1px;
  }
  .divider-top { top: 219px; }
  .divider-bottom { top: 451px; }

  .person { position: absolute; left: 37px; top: 246px; }
  .person-name { font-weight: 700; font-size: 29px; line-height: 32px; }
  .person-name .first { color: var(--red); }
  .person-credentials { font-weight: 700; font-size: 16px; margin-top: 1px; letter-spacing: .2px; }

  .contact { position: absolute; left: 37px; list-style: none; font-size: 13.5px; }
  .contact li { display: flex; align-items: center; height: 22px; }
  .contact svg { width: 15px; height: 15px; margin-right: 7px; flex: none; }
  .contact-phones { top: 320px; }
  .contact-web { top: 374px; }

  .address {
    position: absolute; top: 478px; width: 100%; text-align: center;
    font-style: italic; font-size: 13px;
  }

  .tagline { position: absolute; left: 0; }
  .tagline .bar { position: absolute; left: 0; top: 0; width: 14px; height: 65px; }
  .tagline p { padding-left: 31px; font-size: 29px; line-height: 34px; }
  .tagline strong { font-style: italic; font-weight: 700; display: block; }
  .tag-1 { top: 259px; } .tag-1 .bar { background: var(--gold); }
  .tag-2 { top: 341px; } .tag-2 .bar { background: var(--orange); }
  .tag-3 { top: 421px; } .tag-3 .bar { background: var(--red); }
  .tagline p { margin-top: -6px; }
</style>
</head>
<body>
  <section class="card card-front">
    <div class="brand">
      <div class="brand-mark"></div>
      <div class="brand-name">Quarrystone<br>Ledgerworks</div>
    </div>
    <div class="divider divider-top"></div>

    <div class="person">
      <div class="person-name"><span class="first">Marcus</span> Tenley</div>
      <div class="person-credentials">CFP®, EA, CTC, CEPA</div>
    </div>

    <ul class="contact contact-phones">
      <li>
        <svg viewBox="0 0 16 16" aria-hidden="true"><rect x="4" y="1" width="8" height="14" rx="1.5" fill="none" stroke="#b31b2c" stroke-width="1.6"/><line x1="7" y1="12.5" x2="9" y2="12.5" stroke="#b31b2c" stroke-width="1.4"/></svg>
        (480)517.3082
      </li>
      <li>
        <svg viewBox="0 0 16 16" aria-hidden="true"><rect x="4" y="1" width="8" height="5" fill="none" stroke="#b31b2c" stroke-width="1.4"/><rect x="1" y="6" width="14" height="6" rx="1" fill="#b31b2c"/><rect x="4" y="10" width="8" height="5" fill="#ecebec" stroke="#b31b2c" stroke-width="1.2"/></svg>
        (623) 391.7258
      </li>
    </ul>
    <ul class="contact contact-web">
      <li>
        <svg viewBox="0 0 16 16" aria-hidden="true"><rect x="1" y="3" width="14" height="10" fill="#b31b2c"/><path d="M1 3 L8 9 L15 3" fill="none" stroke="#ecebec" stroke-width="1.2"/></svg>
        mt@QuarrystoneLedgerworks.com
      </li>
      <li>
        <svg viewBox="0 0 16 16" aria-hidden="true"><g fill="none" stroke="#b31b2c" stroke-width="1.3"><circle cx="8" cy="8" r="6.5"/><ellipse cx="8" cy="8" rx="2.8" ry="6.5"/><line x1="1.5" y1="8" x2="14.5" y2="8"/></g></svg>
        www.MarcusRTenley.com
      </li>
    </ul>

    <div class="divider divider-bottom"></div>
    <p class="address">418 W Larkspur Ave Mesa, AZ 85201</p>
  </section>

  <section class="card card-back">
    <div class="tagline tag-1"><span class="bar"></span><p>Complex <strong>Problems.</strong></p></div>
    <div class="tagline tag-2"><span class="bar"></span><p>Simple <strong>Solutions.</strong></p></div>
    <div class="tagline tag-3"><span class="bar"></span><p>Peak <strong>Performance.</strong></p></div>
  </section>
</body>
</html>
```